Compelling Senior Home Care highlight live-in home care and couples care

Compelling High end client who is looking to advertise and highlight their live-in home care and couples care. Their name is Meadowlark Home Health Services and their website is https://www.brambleviewcare.example/ Please use their current website colors and I attached some examples.

Specs:

Non-Medical Care or
Home Health Grid Ad
3.85w x 3h

Ad should have:
LOGO
WEBSITE
PHONE NUMBER
(BUTTON - Find Out More)
Text Variations:
We Give People the Help They Need to Live in the Place They Love (see example for exact look and feel)
Do you or your loved one need care at home?
Live at home as long as possible!
Caregivers You Can Trust
Caregivers That Come On Time
Caregivers That Live with You
High Level Care
Hours Match Your Needs

QRG is produced in Macintosh platform CS6. Please create your ads in these programs. Please submit
your ads in high-resolution camera-ready PDF, TIF or EPS format: 300 DPI at 100% of printed size, all
colors CMYK, all fonts and graphics embedded. Use POSTSCRIPT TYPE 1 fonts when possible, TRUE TYPE
FONTS may not print correctly. If submitting native files, please include all linked graphics and fonts.
NOTE: if your ad is not produced by the QRG Art Staff, a professional Ad Agency or Design firm, and is
not properly constructed for technical electronic digital printing, the final printed product may not print
correctly and may differ from your screen proof. Please flightcheck your ad before submitting to QRG.
Publisher reserves the right to charge for all costs incurred in preparation of material submitted that
does not meet the Elder Amber Ledger digital specifications.
• All colors, logos, and images in your ad need to be CMYK builds at 300 dpi at 100% size
• Construct your file document size to our size specifications and save your PDF to 100% of size

Target Market(s)

Adults taking care of mom and dad

Industry/Entity Type

Home Health Care

Requirements
Nice to have
• PLEASE SEE EXAMPLES
Should not have
• BORING

```html
<!DOCTYPE html>
<html lang="en">
<head>
<meta charset="utf-8">
<title>Meadowlark Home Health Services – Grid Ad</title>
<link rel="stylesheet" href="https://fonts.googleapis.com/css2?family=Montserrat:wght@400;500;700&display=swap">
<style>
  :root {
    --page-bg: #e9eaee;
    --card-bg: #ffffff;
    --plum: #80205f;
    --ink: #170910;
    --white: #ffffff;
  }
  * { margin: 0; padding: 0; box-sizing: border-box; }
  html, body {
    width: 1200px; height: 1200px; overflow: hidden;
    background: var(--page-bg);
    font-family: "Montserrat", sans-serif;
  }
  .ad-card {
    position: absolute; left: 69px; top: 186px;
    width: 1061px; height: 826px;
    background: var(--card-bg);
    box-shadow: 0 6px 18px rgba(0,0,0,0.12);
    overflow: hidden;
  }
  .ad-shapes { position: absolute; inset: 0; }
  .brand {
    position: absolute; left: 60px; top: 52px;
    display: flex; align-items: center; gap: 20px;
    color: var(--plum); font-weight: 700;
  }
  .brand-mark { width: 96px; height: 96px; background: var(--plum); }
  .brand-name { line-height: 1.05; }
  .brand-name .primary { display: block; font-size: 54px; letter-spacing: -0.5px; }
  .brand-name .secondary { display: block; font-size: 22px; margin-top: 8px; }
  .headline {
    position: absolute; left: 61px; top: 556px;
    color: var(--white); text-transform: uppercase;
  }
  .headline .lead { display: block; font-size: 64px; font-weight: 500; line-height: 1; letter-spacing: -0.5px; }
  .headline .sub { display: block; font-size: 44px; font-weight: 400; line-height: 1; margin-top: 14px; letter-spacing: 0.5px; }
  .cta-button {
    position: absolute; left: 57px; top: 710px;
    width: 271px; height: 68px; border-radius: 34px;
    background: var(--ink);
    display: flex; align-items: center; justify-content: center;
  }
  .cta-button::before {
    content: ""; position: absolute; inset: 4px;
    border: 2px solid var(--white); border-radius: 30px;
  }
  .cta-button span { color: var(--white); font-weight: 700; font-size: 25px; letter-spacing: 0.3px; }
  .contact {
    position: absolute; color: var(--plum); font-weight: 400;
    display: flex; align-items: center; gap: 10px; white-space: nowrap;
  }
  .contact svg { flex: none; }
  .contact-phone { left: 584px; top: 704px; font-size: 34px; }
  .contact-web { right: 44px; top: 754px; font-size: 24px; }
</style>
</head>
<body>
<div class="ad-card">
  <svg class="ad-shapes" width="1061" height="826" viewBox="0 0 1061 826">
    <defs>
      <linearGradient id="photoTone" x1="0" y1="0" x2="1" y2="1">
        <stop offset="0" stop-color="#f6f6f6"/>
        <stop offset="0.45" stop-color="#efe8e3"/>
        <stop offset="0.7" stop-color="#dfe3ee"/>
        <stop offset="1" stop-color="#f4f4f5"/>
      </linearGradient>
      <filter id="soft" x="-5%" y="-5%" width="110%" height="115%">
        <feDropShadow dx="0" dy="3" stdDeviation="4" flood-opacity="0.18"/>
      </filter>
    </defs>
    <polygon class="corner-accent" points="861,0 1061,0 1061,208" fill="var(--plum)"/>
    <g role="img" aria-label="Photo of four smiling seniors together in a bright living room">
      <polygon points="0,206 841,206 1017,388 1017,604 0,604" fill="url(#photoTone)" filter="url(#soft)"/>
    </g>
    <polygon class="diagonal-stripe" points="0,217 541,778 508,778 0,251" fill="var(--ink)"/>
    <polygon class="plum-panel" points="0,251 554,826 0,826" fill="var(--plum)"/>
    <polygon class="headline-band" fill="var(--ink)"
      points="0,540 250,533 520,528 470,536 540,534 525,545 560,548 545,560 575,566 560,578 590,590 570,604 600,612 580,626 620,636 590,648 560,654 580,664 540,670 560,680 500,684 300,688 0,690"/>
  </svg>

  <div class="brand">
    <div class="brand-mark"></div>
    <div class="brand-name">
      <span class="primary">Meadowlark</span>
      <span class="secondary">Home Health Services</span>
    </div>
  </div>

  <h1 class="headline">
    <span class="lead">Caregivers</span>
    <span class="sub">You Can Trust</span>
  </h1>

  <div class="cta-button"><span>FIND OUT MORE</span></div>

  <div class="contact contact-phone">
    <svg width="28" height="28" viewBox="0 0 24 24" aria-hidden="true"><path fill="var(--ink)" d="M6.6 10.8a15.1 15.1 0 0 0 6.6 6.6l2.2-2.2c.3-.3.7-.4 1-.2 1.1.4 2.3.6 3.6.6.6 0 1 .4 1 1V20c0 .6-.4 1-1 1A17 17 0 0 1 3 4c0-.6.4-1 1-1h3.5c.6 0 1 .4 1 1 0 1.3.2 2.5.6 3.6.1.3 0 .7-.2 1z"/></svg>
    <span>555-014-2290</span>
  </div>
  <div class="contact contact-web">
    <svg width="24" height="24" viewBox="0 0 24 24" aria-hidden="true"><g fill="none" stroke="var(--ink)" stroke-width="2"><circle cx="12" cy="12" r="10" fill="var(--ink)"/><path stroke="var(--white)" stroke-width="1.2" d="M2 12h20M12 2c3 3 3 17 0 20M12 2c-3 3-3 17 0 20M4 7h16M4 17h16"/></g></svg>
    <span>www.BrambleviewCare.example</span>
  </div>
</div>
</body>
</html>
```